Blue Heron Courier & Delivery Services needs a flyer

We need an introductory flyer for a new company based in Yellowknife, Northwest Territories,Canada. Our company name is Blue Heron Courier & Delivery Services. We will be handling envelopes and small packages up to 20 pounds. We expect 20 percent of our business to come from residential customers and 80 percent from the business community including lawyers, doctors, engineers and government offices. The main message that we will try to convey in this flyer is that we are a new and exciting company that promises to make 100% customer satisfaction our number one goal. I would like the layout to be elegant and simple and certainly not cluttered. It will be a single sided flyer. Text should be easy to read and most likely at most two fonts. I would like one stunning image or photo relating to the courier business and message. There should be plenty of white space throughout the flyer and nice margins on all sides. I would like my flyer to be 8.5 inches by 11 inches and it should read from top to bottom. . I would like a nice big bold headline that in some way mentions " Special Offer- Up to 100% Off. You can change the wording if you have a better idea. Throughout the flyer you can highlight and italicize for emphasis. Please try to use bullet points for my five main reasons for hiring our company which are: you will be 100% satisfied with each delivery or you will be given a complete refund no questions asked, your envelope or package will be delivered on time every time, you will always be treated throughout the delivery process in a professional manner, you will be given the widest selection in Yellowknife of price points and delivery options , you can trust us with your most important and time sensitive deliveries. Try to incorporate something next to these five points to really draw attention like a check mark, star etc.... I would prefer if my company name and contact info is in the bottom third of the flyer. My email is blueheroncourieryk@mailbox-example.net. My phone number is 867-312-7794. It might be a good idea to have my phone number also at the top of the flyer someplace after the headline saying like Call Now!!! you can use boxes, borders and contrasting bold colors to bring flyer to life. I have a testimonial from a business owner that I dealt with when I ran another business which would be nice to have included . " While receiving daily deliveries for 18 years from Calvin Marsh I found him to be punctual , reliable and efficient " Glen Potter, owner of Potter and Lindqvist Trading LTD, Yellowknife,NWT. I thought perhaps at the top of flyer after the headline perhaps in some way you could say Yellowknife's newest and best courier and delivery service is pleased to offer the following stunning discounts: then you could list the three special offers: 1) First 5 businesses to book regular scheduled deliveries will get 100% off their first delivery. 2) First 5 businesses to book a single delivery will get 50% off that delivery. 3) First 5 residential customers to book a delivery will receive 25% off that delivery. I thought you could mention my name somewhere. Calvin Marsh. Owner has lived in Yellowknife for 42 years and has 20 years experience doing performing important and time sensitive deliveries. Perhaps you could mention somewhere that we will have a couple of ongoing discounts also which will be 1) seniors discounts. 2) regular scheduled deliveries discounts. I have suggested colors but if you have other ideas I would certainly look at them. Our business tag line is. On Time Every Time
Target Market(s)
Business owners typically males 30-50 years old
Industry/Entity Type
Delivery Service
Requirements
Must have
- Done in CMYK mode sufficient bleed size for printing
Nice to have
- Nothing set in stone. I recently had my logo design uploaded to this brief. It is up to you if you feel it should be included in the flyer.
Should not have
- I am willing to look at any design

```html
<!DOCTYPE html>
<html lang="en">
<head>
<meta charset="utf-8">
<title>Blue Heron Courier &amp; Delivery Services – Special Offer Flyer</title>
<link href="https://fonts.googleapis.com/css2?family=Montserrat:wght@800;900&family=Arimo:ital,wght@0,400;0,700;1,400;1,700&family=Questrial&display=swap" rel="stylesheet">
<style>
  :root {
    --ink: #06121a;
    --deep: #0a2a38;
    --teal: #0f5f7a;
    --teal-bright: #1d86a6;
    --sky: #19b4ea;
    --white: #ffffff;
    --tagline: #0d3f52;
    --alert: #e8412f;
  }
  * { box-sizing: border-box; margin: 0; padding: 0; }
  html, body { width: 960px; height: 1200px; overflow: hidden; background: var(--ink); }
  .flyer {
    position: relative; width: 960px; height: 1200px; overflow: hidden;
    color: var(--white); font-family: "Questrial", sans-serif;
    background:
      linear-gradient(160deg, var(--ink) 0%, var(--deep) 22%, var(--teal) 48%, var(--deep) 70%, var(--ink) 100%);
  }
  .headline {
    position: absolute; left: 20px; top: 34px;
    font-family: "Montserrat", sans-serif; font-weight: 900; font-size: 47px;
    letter-spacing: 1px; color: var(--sky);
    transform: rotate(-1.6deg); transform-origin: left bottom; white-space: nowrap;
  }
  .headline .highlight { color: var(--white); }
  .chevrons { position: absolute; left: 20px; top: 116px; }
  .call-box {
    position: absolute; left: 553px; top: 118px; width: 407px; height: 63px;
    background: var(--teal); display: flex; align-items: center; justify-content: center;
    font-family: "Arimo", sans-serif; font-size: 25px; white-space: nowrap;
  }
  .call-box strong { font-family: "Montserrat", sans-serif; font-weight: 800; letter-spacing: 1px; margin-left: 8px; }
  .intro {
    position: absolute; left: 19px; top: 218px; width: 940px;
    font-family: "Arimo", sans-serif; font-weight: 700; font-size: 25.5px; line-height: 31px;
    color: var(--sky); text-transform: uppercase;
  }
  .offers { position: absolute; left: 36px; top: 313px; list-style: none; }
  .offers li { position: relative; padding-left: 36px; font-size: 19px; height: 31px; line-height: 26px; }
  .offers li::before { content: ""; position: absolute; left: 0; top: 7px; width: 13px; height: 13px; border-radius: 50%; background: var(--white); }
  .offers strong { font-family: "Arimo", sans-serif; font-weight: 700; }
  .ongoing {
    position: absolute; left: 703px; top: 417px; width: 257px; height: 153px;
    background: rgba(29,134,166,.55); padding: 18px 0 0 29px; border-radius: 4px 0 0 4px;
  }
  .ongoing h3 { font-family: "Montserrat", sans-serif; font-weight: 800; font-size: 23px; letter-spacing: 1px; }
  .ongoing ul { list-style: none; margin-top: 8px; }
  .ongoing li { position: relative; padding-left: 40px; font-size: 17px; line-height: 21px; margin-bottom: 11px; letter-spacing: .3px; }
  .ongoing li::before { content: "•"; position: absolute; left: 13px; }
  .why-title { position: absolute; left: 19px; top: 483px; font-family: "Arimo", sans-serif; font-weight: 700; font-size: 25px; color: var(--sky); }
  .reasons { position: absolute; left: 28px; top: 528px; list-style: none; }
  .reasons li { position: relative; height: 70px; padding-left: 53px; font-family: "Arimo", sans-serif; font-style: italic; font-size: 19px; line-height: 24px; }
  .reasons strong { font-weight: 700; }
  .reasons svg { position: absolute; left: 0; top: 4px; }
  .courier-visual {
    position: absolute; left: 566px; top: 647px; width: 394px; height: 553px;
    background: radial-gradient(ellipse at 55% 45%, rgba(3,14,20,.85) 0%, rgba(5,22,30,.55) 45%, rgba(10,42,56,0) 75%);
  }
  .footer-band { position: absolute; left: 0; top: 922px; width: 960px; height: 205px; background: rgba(5,16,22,.9); }
  .footer-strip { position: absolute; left: 0; top: 1127px; width: 960px; height: 73px; background: linear-gradient(90deg, var(--ink) 0%, var(--teal) 70%, var(--teal-bright) 100%); }
  .brand { position: absolute; left: 19px; top: 956px; }
  .brand-name { font-family: "Arimo", sans-serif; font-weight: 700; font-size: 58px; line-height: 56px; color: var(--sky); letter-spacing: -.5px; }
  .brand-sub { font-family: "Arimo", sans-serif; font-weight: 700; font-size: 26px; line-height: 28px; }
  .brand-tagline { font-family: "Arimo", sans-serif; font-size: 50px; line-height: 58px; color: var(--tagline); letter-spacing: -3px; margin-top: 4px; }
  .contact { position: absolute; left: 528px; top: 942px; width: 420px; }
  .contact h4 { font-family: "Questrial", sans-serif; font-weight: 400; font-size: 18px; color: var(--alert); }
  .contact-line { display: flex; align-items: center; gap: 10px; font-size: 16.5px; color: var(--alert); margin-top: 8px; }
  .contact-line.phone { letter-spacing: 2.5px; font-size: 17px; }
  .owner-bio { margin-top: 12px; font-family: "Arimo", sans-serif; font-size: 17.5px; line-height: 22px; }
</style>
</head>
<body>
<main class="flyer">
  <h1 class="headline">SPECIAL OFFER- UP TO <span class="highlight">100% OFF</span></h1>

  <svg class="chevrons" width="180" height="30" viewBox="0 0 180 30" aria-hidden="true">
    <g fill="none" stroke-width="5" stroke-linecap="square">
      <path d="M4 5 L15 16 L4 27" stroke="#fff"/>
      <path d="M58 3 L69 14 L58 25" stroke="#19b4ea"/>
      <path d="M110 2 L121 13 L110 24" stroke="#fff"/>
      <path d="M163 1 L174 12 L163 23" stroke="#19b4ea"/>
    </g>
  </svg>

  <div class="call-box">CALL NOW!!! - <strong>867-312-7794</strong></div>

  <p class="intro">Yellowknife's newest and best courier and delivery service<br>is pleased to offer the following stunning discounts:</p>

  <ul class="offers">
    <li><strong>GET 100% OFF</strong> for first 5 businesses to book regular scheduled deliveries.</li>
    <li><strong>GET 50% OFF</strong> for first 5 businesses to book a single delivery.</li>
    <li><strong>GET 25% OFF</strong> for first 5 residential customers to book a delivery.</li>
  </ul>

  <aside class="ongoing">
    <h3>ONGOING!</h3>
    <ul>
      <li>seniors discounts.</li>
      <li>regular scheduled deliveries discounts</li>
    </ul>
  </aside>

  <div class="courier-visual" role="img" aria-label="Dark silhouette of a courier in a cap running while holding out a package"></div>

  <h2 class="why-title">WHY HIRE US?</h2>
  <ul class="reasons">
    <li><svg width="42" height="36" viewBox="0 0 42 36" aria-hidden="true"><path d="M3 15 H11 V33 H3 Z M11 16 L20 4 Q23 1 24 5 L22 14 H37 Q40 15 39 18 L36 31 Q35 33 32 33 H11" fill="none" stroke="#fff" stroke-width="2.4" stroke-linejoin="round"/></svg>You will be <strong>100% SATISFIED</strong> with each delivery or you<br>will be given a <strong>COMPLETE REFUND</strong> no questions asked.</li>
    <li><svg width="42" height="36" viewBox="0 0 42 36" aria-hidden="true"><path d="M3 15 H11 V33 H3 Z M11 16 L20 4 Q23 1 24 5 L22 14 H37 Q40 15 39 18 L36 31 Q35 33 32 33 H11" fill="none" stroke="#fff" stroke-width="2.4" stroke-linejoin="round"/></svg>Your envelope or package will be delivered<br><strong>ON TIME EVERY TIME</strong>.</li>
    <li><svg width="42" height="36" viewBox="0 0 42 36" aria-hidden="true"><path d="M3 15 H11 V33 H3 Z M11 16 L20 4 Q23 1 24 5 L22 14 H37 Q40 15 39 18 L36 31 Q35 33 32 33 H11" fill="none" stroke="#fff" stroke-width="2.4" stroke-linejoin="round"/></svg>You will always be <strong>TREATED</strong> throughout the<br>delivery process <strong>IN A PROFESSIONAL MANNER</strong>.</li>
    <li><svg width="42" height="36" viewBox="0 0 42 36" aria-hidden="true"><path d="M3 15 H11 V33 H3 Z M11 16 L20 4 Q23 1 24 5 L22 14 H37 Q40 15 39 18 L36 31 Q35 33 32 33 H11" fill="none" stroke="#fff" stroke-width="2.4" stroke-linejoin="round"/></svg>You will be given the <strong>WIDEST SELECTION</strong> in<br>Yellowknife <strong>OF PRICE POINTS AND DELIVERY OPTIONS</strong>.</li>
    <li><svg width="42" height="36" viewBox="0 0 42 36" aria-hidden="true"><path d="M3 15 H11 V33 H3 Z M11 16 L20 4 Q23 1 24 5 L22 14 H37 Q40 15 39 18 L36 31 Q35 33 32 33 H11" fill="none" stroke="#fff" stroke-width="2.4" stroke-linejoin="round"/></svg><strong>YOU CAN TRUST US</strong> with your most important<br>and time sensitive deliveries within the city of Yellowknife.</li>
  </ul>

  <div class="footer-band"></div>
  <div class="footer-strip"></div>

  <div class="brand">
    <div class="brand-name">BLUE HERON</div>
    <div class="brand-sub">COURIER &amp; DELIVERY SERVICES</div>
    <div class="brand-tagline">ON TIME EVERY TIME</div>
  </div>

  <section class="contact">
    <h4>CONTACT INFO</h4>
    <div class="contact-line">
      <svg width="30" height="18" viewBox="0 0 30 18" aria-hidden="true"><rect x="1" y="1" width="20" height="15" fill="none" stroke="#e8412f" stroke-width="1.6"/><path d="M1 1 L11 9 L21 1" fill="none" stroke="#e8412f" stroke-width="1.6"/><circle cx="25" cy="12" r="4" fill="none" stroke="#e8412f" stroke-width="1.6"/></svg>
      blueheroncourieryk@mailbox-example.net
    </div>
    <div class="contact-line phone">
      <svg width="22" height="20" viewBox="0 0 22 20" aria-hidden="true"><rect x="0" y="0" width="22" height="20" rx="3" fill="#e8412f"/><path d="M7 4 Q5 5 6 9 Q8 14 13 16 Q16 17 17 15 L15 12 L13 13 Q10 11 9 8 L10 6 Z" fill="#06121a"/></svg>
      867-312-7794.
    </div>
    <p class="owner-bio">Calvin Marsh. Owner has lived in Yellowknife for 42 years and has 20 years experience performing important and time sensitive deliveries.</p>
  </section>
</main>
</body>
</html>
```